Business Card for Managing Partner Investment Fund

To create a business card template for an investment fund manager. Business card should be more professional in nature, not too colorful, more upscale, and created using the attached logos and fund name files. I would prefer a black or gray color scheme, but am open to the use of color as well. I would prefer a double sided business card, but open to single sided business card designs as well. The business card should include: name, title, and contact information, as well as logo and company name. I would prefer a more stream-lined, simple business card design.
Updates
Address: 4190 NE 38th Ter. Ocala, FL 34470
Email: talvin47@quorimail.net
Phone: 561-347-9162
Title: managing partner
Name: Dorian Velsky
Fund Name: Ambergate Capital
Logos can be found in files attached to the brief
Target Market(s)
potential investors, other fund managers
Industry/Entity Type
Finance
Contact Information for Business Card
Name on card: Dorian Velsky
Title: Managing Partner
Colors
Designer to choose colors to be used in the design.
Requirements
Must have
- Phone number
- email address
- physical address
- title
- name
- logo
- Fund name
Nice to have
- simple layout
Should not have
- too many colors, busy fonts,

```html
<!DOCTYPE html>
<html lang="en">
<head>
<meta charset="utf-8">
<title>Ambergate Capital – Business Card</title>
<link href="https://fonts.googleapis.com/css2?family=Roboto:wght@400;500&display=swap" rel="stylesheet">
<style>
  :root {
    --backdrop: #2b3134;
    --charcoal: #3f4042;
    --sand: #b3a483;
    --ink: #3a3b3d;
    --paper: #ffffff;
    --cream: #d9cfb8;
  }
  * { box-sizing: border-box; margin: 0; padding: 0; }
  html, body { width: 1200px; height: 1200px; overflow: hidden; }
  body {
    background: var(--backdrop);
    font-family: "Roboto", Arial, sans-serif;
    position: relative;
  }
  .card {
    position: absolute;
    left: 253px;
    width: 693px;
    height: 416px;
    overflow: hidden;
  }
  .card--front { top: 100px; background: var(--sand); }
  .card--back { top: 596px; background: var(--charcoal); }
  .card__shapes { position: absolute; inset: 0; }

  .identity { position: absolute; left: 304px; top: 82px; color: var(--ink); }
  .identity__name { font-size: 28px; font-weight: 500; letter-spacing: 0.3px; line-height: 32px; text-transform: uppercase; }
  .identity__title { font-size: 18px; font-weight: 400; margin-left: 5px; line-height: 20px; }

  .contacts { position: absolute; left: 42px; top: 232px; list-style: none; }
  .contacts__item { display: flex; align-items: center; height: 34px; margin-bottom: 11px; font-size: 17px; color: var(--ink); font-weight: 500; }
  .contacts__icon { width: 34px; height: 34px; margin-right: 6px; flex: none; }

  .brand {
    position: absolute;
    font-weight: 500;
    text-transform: uppercase;
    white-space: nowrap;
    transform: translateX(-50%);
  }
  .brand--front { left: 564px; top: 290px; color: var(--paper); font-size: 17px; letter-spacing: 2px; }
  .brand--back { left: 339px; top: 212px; color: var(--cream); font-size: 26px; letter-spacing: 3px; }
</style>
</head>
<body>
  <section class="card card--front">
    <svg class="card__shapes" viewBox="0 0 693 416" width="693" height="416" aria-hidden="true">
      <polygon fill="var(--charcoal)" points="202,0 252,80 547,80 600,136 292,136 480,416 693,416 693,0"/>
    </svg>
    <div class="identity">
      <p class="identity__name">Dorian Velsky</p>
      <p class="identity__title">managing partner</p>
    </div>
    <ul class="contacts">
      <li class="contacts__item">
        <svg class="contacts__icon" viewBox="0 0 34 34" aria-hidden="true">
          <circle cx="17" cy="17" r="17" fill="var(--charcoal)"/>
          <path d="M9 14c0-3 4-4 8-4s8 1 8 4v2h-4v-2h-8v2H9z M11 17h12l2 7H9z" fill="var(--sand)"/>
          <circle cx="17" cy="20" r="2" fill="var(--charcoal)"/>
        </svg>
        561-347-9162
      </li>
      <li class="contacts__item">
        <svg class="contacts__icon" viewBox="0 0 34 34" aria-hidden="true">
          <circle cx="17" cy="17" r="17" fill="var(--charcoal)"/>
          <rect x="9" y="11" width="16" height="12" fill="none" stroke="var(--sand)" stroke-width="1.5"/>
          <path d="M9 11l8 7 8-7 M9 23l6-6 M25 23l-6-6" fill="none" stroke="var(--sand)" stroke-width="1.5"/>
        </svg>
        talvin47@quorimail.net
      </li>
      <li class="contacts__item">
        <svg class="contacts__icon" viewBox="0 0 34 34" aria-hidden="true">
          <circle cx="17" cy="17" r="17" fill="var(--charcoal)"/>
          <path d="M17 8a6 6 0 0 1 6 6c0 5-6 12-6 12s-6-7-6-12a6 6 0 0 1 6-6z" fill="var(--sand)"/>
          <circle cx="17" cy="14" r="2.3" fill="var(--charcoal)"/>
        </svg>
        4190 NE 38th Ter. Ocala, FL 34470
      </li>
    </ul>
    <p class="brand brand--front">Ambergate Capital</p>
  </section>

  <section class="card card--back">
    <svg class="card__shapes" viewBox="0 0 693 416" width="693" height="416" aria-hidden="true">
      <polygon fill="var(--sand)" points="487,0 693,0 693,416 207,416"/>
    </svg>
    <p class="brand brand--back">Ambergate Capital</p>
  </section>
</body>
</html>
```